Pet sitting Business needs a website

We need a website that shows our services and prices. Shows our love of animals but also our professionalism. want a gallery, about, blog, services, links to fb and instagram accounts, newsletter archive. want it to be easy to access and wonderful to navigate. want the domain to be Birchvalecritterden.com
take any info from FB site www.facebook.com/birchvalecritterden
I would like it to fit tidy frame platform

Target Market(s)

upscale area, responsible pet owners,

Industry/Entity Type

Pet Care

Coding

Coded - Design and coding required

Number of Pages Required

5+ page

Font styles to use
Sans Serif

Requirements
Must have
• (tidy frame platform)
• Menu
• photo gallery
• about us
• services
• policies
• monthly newsletter
• unavailable dates
• Introduction (welcome)
• payment methods
• Daily updates
• testimonials (use from fb site)
Should not have
• stock photos

```html
<!DOCTYPE html>
<html lang="en">
<head>
<meta charset="utf-8">
<title>Birchvale Critter Den</title>
<link href="https://fonts.googleapis.com/css2?family=Open+Sans:ital,wght@0,400;0,600;0,700;0,800;1,400;1,600;1,700&display=swap" rel="stylesheet">
<style>
:root{
  --blue:#0b6aa3;
  --blue-dark:#095a8b;
  --nav:#0e74b0;
  --orange:#d98b00;
  --orange-dark:#a96400;
  --brown:#6b3500;
  --paper:#f2f2f2;
  --ink:#555;
  --body:#666;
  --white:#fff;
}
*{margin:0;padding:0;box-sizing:border-box}
html,body{width:1200px;height:3321px;overflow:hidden}
body{position:relative;background:var(--paper);font-family:"Open Sans",sans-serif;color:var(--ink)}
.abs{position:absolute}

/* header */
.top-rule{left:0;top:0;width:1200px;height:5px;background:var(--blue)}
.brand{left:75px;top:64px;display:flex;align-items:center;gap:12px}
.brand-dot{width:36px;height:36px;border-radius:50%;background:var(--orange)}
.brand-name{font-size:24px;font-weight:700;color:var(--orange)}
.contact-chip{top:52px;height:38px;display:flex;align-items:center;gap:12px;font-size:16px;font-weight:700;color:var(--orange)}
.chip-icon{width:38px;height:38px;border:2px solid var(--orange);border-radius:50%;display:flex;align-items:center;justify-content:center}

/* nav */
.nav{left:0;top:140px;width:1200px;height:60px;background:var(--nav);border-bottom:4px solid var(--blue-dark)}
.nav-item{top:0;height:56px;display:flex;align-items:center;justify-content:center;color:var(--white);font-size:12.5px;font-weight:700;text-transform:uppercase;letter-spacing:.2px;white-space:nowrap}
.nav-item.active{background:var(--orange)}

/* hero */
.hero{left:0;top:200px;width:1200px;height:497px;background:
  radial-gradient(ellipse 520px 260px at 600px 330px,rgba(120,80,45,.55),rgba(120,80,45,0) 70%),
  linear-gradient(180deg,#3e4a2c 0%,#5f7440 22%,#84a05a 50%,#9cb46a 75%,#a9bb72 100%)}
.hero-title{left:0;top:378px;width:1200px;text-align:center;color:var(--white);font-size:41px;font-weight:800;line-height:54px;text-transform:uppercase;letter-spacing:.5px;text-shadow:0 2px 4px rgba(0,0,0,.45)}
.hero-sub{left:0;top:428px;width:1200px;text-align:center;color:var(--white);font-size:26px;font-weight:600;line-height:38px;text-shadow:0 2px 4px rgba(0,0,0,.45)}
.btn{display:flex;align-items:center;justify-content:center;background:var(--orange);color:var(--white);font-size:13px;font-weight:700;text-transform:uppercase;border-bottom:3px solid var(--orange-dark)}
.hero-btn{left:524px;top:500px;width:152px;height:50px}
.dots{left:564px;top:636px;display:flex;gap:8px}
.dots span{width:12px;height:12px;border-radius:50%;background:var(--white)}
.dots span.on{background:var(--blue)}

/* section headings */
.mark{width:30px;height:30px;border-radius:50%;background:var(--orange)}
.mark.light{background:var(--white)}
.rule{width:84px;height:3px;background:var(--blue)}
.rule.light{background:var(--white)}
.heading{left:0;width:1200px;text-align:center;font-size:23px;line-height:32px;font-weight:700;text-transform:uppercase;letter-spacing:.5px}

/* welcome */
.welcome-lead{left:90px;top:856px;width:1020px;text-align:center;color:var(--blue);font-size:16.5px;font-weight:600;line-height:27px}
.welcome-body{left:100px;top:916px;width:1000px;text-align:center;font-size:14px;line-height:27px;color:var(--body)}

/* gallery */
.gallery{left:0;top:1127px;width:1200px;height:562px;background:var(--blue)}

/* news */
.news-img{top:1875px;width:330px;height:206px}
.news-title{top:2108px;width:330px;color:var(--blue);font-size:16px;font-weight:700;text-transform:uppercase;line-height:27px}
.news-date{top:2165px;color:var(--orange);font-size:12px;font-weight:600;display:flex;align-items:center;gap:6px}
.news-text{top:2187px;width:330px;font-size:14px;line-height:26px;color:var(--body)}

/* testimonials */
.testimonials{left:0;top:2309px;width:1200px;height:461px;background:var(--orange)}
.quote{top:2484px;width:330px;color:var(--white);font-size:14px;font-style:italic;line-height:26px}
.quote b{font-style:normal;font-weight:800;margin-right:4px}
.author{top:2635px;display:flex;align-items:flex-start;gap:10px}
.avatar{width:66px;height:66px}
.author-name{width:258px;font-size:14px;font-style:italic;font-weight:700;line-height:26px;padding-top:9px;color:var(--brown)}
.author-name span{color:var(--white)}

/* newsletter */
.signup{left:257px;top:2953px;width:688px;height:47px;display:flex;border:1px solid #ccc;background:var(--white)}
.signup-field{flex:1;display:flex;align-items:center;gap:14px;padding-left:14px;font-size:13px;color:#888}
.signup-btn{width:104px;background:var(--blue);color:var(--white);font-size:14px;font-weight:700;display:flex;align-items:center;justify-content:center;text-transform:uppercase}

/* footer */
.footer{left:0;top:3040px;width:1200px;height:232px;background:var(--blue)}
.foot-brand{left:75px;top:3100px;display:flex;align-items:center;gap:10px}
.foot-brand i{width:20px;height:20px;border-radius:50%;background:var(--white)}
.foot-brand span{font-size:17px;font-weight:700;color:var(--white)}
.foot-about{left:75px;top:3170px;width:268px;font-size:13.5px;line-height:21.5px;color:var(--white)}
.foot-h{top:3080px;font-size:16px;line-height:22px;font-weight:700;color:var(--orange);text-transform:uppercase;letter-spacing:.4px}
.foot-list{top:3104px;list-style:none;font-size:13.5px;line-height:26px;color:var(--white)}
.foot-line{left:906px;font-size:13.5px;line-height:21.5px;color:var(--white);display:flex;align-items:center;gap:8px}

.bottom-bar{left:0;top:3272px;width:1200px;height:49px;background:var(--orange)}
.copy{left:75px;top:3287px;font-size:11.5px;line-height:16px;color:var(--brown)}
.socials{left:917px;top:3283px;display:flex;gap:9px}
.socials span{width:26px;height:26px;border-radius:50%;background:var(--blue);border:2px solid rgba(255,255,255,.55)}
</style>
</head>
<body>
<div class="abs top-rule"></div>

<div class="abs brand"><span class="brand-dot"></span><span class="brand-name">Birchvale Critter Den</span></div>
<div class="abs contact-chip" style="left:642px">
  <span class="chip-icon"><svg width="18" height="18" viewBox="0 0 24 24" fill="none" stroke="#d98b00" stroke-width="2.2"><path d="M5 3h4l2 5-3 2a11 11 0 0 0 6 6l2-3 5 2v4a2 2 0 0 1-2 2A17 17 0 0 1 3 5a2 2 0 0 1 2-2z"/></svg></span>1-800-555-0142</div>
<div class="abs contact-chip" style="left:856px">
  <span class="chip-icon"><svg width="18" height="18" viewBox="0 0 24 24" fill="none" stroke="#d98b00" stroke-width="2.2"><rect x="3" y="5" width="18" height="14" rx="1"/><path d="M3 6l9 7 9-7"/></svg></span>info@birchvalecritterden.com</div>

<nav class="abs nav">
  <div class="abs nav-item active" style="left:75px;width:62px">Home</div>
  <div class="abs nav-item" style="left:176px;width:88px">About Us</div>
  <div class="abs nav-item" style="left:297px;width:84px">Services</div>
  <div class="abs nav-item" style="left:415px;width:132px">Photo Gallery</div>
  <div class="abs nav-item" style="left:580px;width:98px">Club News</div>
  <div class="abs nav-item" style="left:712px;width:82px">Policies</div>
  <div class="abs nav-item" style="left:826px;width:162px">Unavailable Dates</div>
  <div class="abs nav-item" style="left:1022px;width:104px">Contact Us</div>
</nav>

<section class="abs hero" role="img" aria-label="Photo of four dogs sitting together on a sunny lawn"></section>
<h1 class="abs hero-title">Birchvale Critter Den</h1>
<p class="abs hero-sub">We provide professional pet sitting services</p>
<div class="abs btn hero-btn">Read More</div>
<div class="abs dots"><span class="on"></span><span></span><span></span><span></span></div>

<div class="abs mark" style="left:585px;top:733px"></div>
<div class="abs rule" style="left:558px;top:785px"></div>
<h2 class="abs heading" style="top:810px;color:var(--orange)">Welcome to our website</h2>
<p class="abs welcome-lead">The biggest key is to make people aware that I was a Licensed Veterinarian Technician from Riverton, Or. That is a huge “selling” point when hiring someone to care for your pets.</p>
<p class="abs welcome-body">Instead of feeling guilty when you must leave your pet for long work days, travel or appointments you can feel good knowing that you have provided your pet with a best friend, Birchvale Critter Den.</p>
<div class="abs btn" style="left:524px;top:1018px;width:152px;height:52px">Read More</div>

<section class="abs gallery"></section>
<div class="abs mark light" style="left:585px;top:1172px"></div>
<div class="abs rule light" style="left:558px;top:1223px"></div>
<h2 class="abs heading" style="top:1248px;color:var(--white)">Photo Gallery</h2>
<div class="abs" style="left:75px;top:1324px;width:253px;height:150px;background:linear-gradient(135deg,#8a5f3c,#c9a07a 55%,#e3c8a8)" role="img" aria-label="Photo of a small dog and a corgi on a wooden floor"></div>
<div class="abs" style="left:75px;top:1490px;width:253px;height:153px;background:linear-gradient(160deg,#b08a68,#e8d6c4 50%,#c99a6c)" role="img" aria-label="Photo of a cat lounging on a floor"></div>
<div class="abs" style="left:341px;top:1324px;width:251px;height:319px;background:linear-gradient(170deg,#6b4a38,#c98d52 45%,#e6d6bc 80%,#5a3a28)" role="img" aria-label="Photo of a pet sitter with two golden dogs"></div>
<div class="abs" style="left:609px;top:1324px;width:250px;height:319px;background:radial-gradient(ellipse at 50% 55%,#e8dcc8,#c08a48 55%,#9a6a30)" role="img" aria-label="Close-up photo of a dog on a tiled floor"></div>
<div class="abs" style="left:875px;top:1324px;width:250px;height:150px;background:linear-gradient(135deg,#9a8e80,#2e2a28 55%,#6e6258)" role="img" aria-label="Photo of a black dog indoors"></div>
<div class="abs" style="left:875px;top:1490px;width:250px;height:153px;background:linear-gradient(135deg,#3a3a3a,#bcbcbc 50%,#f0f0f0)" role="img" aria-label="Black and white photo of two dogs"></div>

<div class="abs mark" style="left:585px;top:1723px"></div>
<div class="abs rule" style="left:558px;top:1775px"></div>
<h2 class="abs heading" style="top:1800px;color:var(--orange)">Club News</h2>

<div class="abs news-img" style="left:75px;background:radial-gradient(ellipse at 55% 55%,#f2ece4,#b8662e 45%,#2a1c14)" role="img" aria-label="Photo of a spaniel puppy"></div>
<div class="abs news-img" style="left:436px;background:linear-gradient(180deg,#d4e6f4,#9cc0de 45%,#6f5640 60%,#7aa0b8)" role="img" aria-label="Photo of a dog by a lake"></div>
<div class="abs news-img" style="left:795px;background:radial-gradient(ellipse at 50% 45%,#d8c6b0,#5e4a3c 50%,#1e1612)" role="img" aria-label="Photo of a Siamese cat"></div>

<h3 class="abs news-title" style="left:75px">Duis aliquam nibh a dui iaculis viverra id a velit</h3>
<h3 class="abs news-title" style="left:436px">Duis aliquam nibh a dui iaculis viverra id a velit</h3>
<h3 class="abs news-title" style="left:795px">Duis aliquam nibh a dui iaculis viverra id a velit</h3>
<div class="abs news-date" style="left:75px"><svg width="12" height="12" viewBox="0 0 12 12"><rect x="1" y="2" width="10" height="9" fill="#d98b00"/></svg>Aug 18, 2016</div>
<div class="abs news-date" style="left:436px"><svg width="12" height="12" viewBox="0 0 12 12"><rect x="1" y="2" width="10" height="9" fill="#d98b00"/></svg>Aug 18, 2016</div>
<div class="abs news-date" style="left:795px"><svg width="12" height="12" viewBox="0 0 12 12"><rect x="1" y="2" width="10" height="9" fill="#d98b00"/></svg>Aug 18, 2016</div>
<p class="abs news-text" style="left:75px">Vestibulum ante ipsum primis in faucibus orci luctus et ultrices posuere cubilia lobortis turpis in odio blandit ac interdum..</p>
<p class="abs news-text" style="left:436px">Vestibulum ante ipsum primis in faucibus orci luctus et ultrices posuere cubilia lobortis turpis in odio blandit ac interdum..</p>
<p class="abs news-text" style="left:795px">Vestibulum ante ipsum primis in faucibus orci luctus et ultrices posuere cubilia lobortis turpis in odio blandit ac interdum..</p>

<section class="abs testimonials"></section>
<div class="abs rule light" style="left:558px;top:2397px"></div>
<h2 class="abs heading" style="top:2422px;color:var(--white)">Testimonials</h2>
<p class="abs quote" style="left:75px"><b>“</b>Hi my name is Dana Whitfield and I would love to introduce myself. I am a Licensed Veterinarian Technician from Riverton, Oregon. My family and I moved to Birchvale in 2008...”</p>
<p class="abs quote" style="left:436px"><b>“</b>Hi my name is Dana Whitfield and I would love to introduce myself. I am a Licensed Veterinarian Technician from Riverton, Oregon. My family and I moved to Birchvale in 2008...”</p>
<p class="abs quote" style="left:795px"><b>“</b>Hi my name is Dana Whitfield and I would love to introduce myself. I am a Licensed Veterinarian Technician from Riverton, Oregon. My family and I moved to Birchvale in 2008...”</p>
<div class="abs author" style="left:75px"><div class="avatar" style="background:linear-gradient(135deg,#4a3428,#b48a6a)" role="img" aria-label="Client photo with her dog"></div><div class="author-name">Biscuit Dog and my Partner Pepper <span>(aka:Mae)</span></div></div>
<div class="abs author" style="left:436px"><div class="avatar" style="background:linear-gradient(135deg,#3e6a80,#c8b49a)" role="img" aria-label="Client photo with her dog"></div><div class="author-name">Biscuit Dog and my Partner Pepper <span>(aka:Mae)</span></div></div>
<div class="abs author" style="left:795px"><div class="avatar" style="background:linear-gradient(135deg,#5a4a30,#d8c08a)" role="img" aria-label="Client photo with her dog"></div><div class="author-name">Biscuit Dog and my Partner Pepper <span>(aka:Mae)</span></div></div>

<div class="abs mark" style="left:585px;top:2828px"></div>
<div class="abs rule" style="left:558px;top:2878px"></div>
<h2 class="abs heading" style="top:2900px;color:var(--orange)">Newsletter Sign Up</h2>
<div class="abs" style="left:0;top:2878px;width:255px;height:162px;background:radial-gradient(ellipse 150px 95px at 110px 100px,#b8824e 0%,#8a7664 55%,rgba(242,242,242,0) 100%)" role="img" aria-label="Photo of a dog and a cat lying together"></div>
<div class="abs" style="left:948px;top:2872px;width:252px;height:168px;background:radial-gradient(ellipse 150px 110px at 130px 100px,#a68058 0%,#9c9ea6 55%,rgba(242,242,242,0) 100%)" role="img" aria-label="Photo of a terrier and a grey cat"></div>
<div class="abs signup">
  <div class="signup-field"><svg width="24" height="18" viewBox="0 0 24 18"><rect x="1" y="1" width="22" height="16" fill="#ccc"/><path d="M1 1l11 9 11-9" fill="none" stroke="#fff" stroke-width="2"/></svg>Enter Email Address</div>
  <div class="signup-btn">Sign Up</div>
</div>

<footer class="abs footer"></footer>
<div class="abs foot-brand"><i></i><span>Birchvale Critter Den</span></div>
<p class="abs foot-about">Duis aliquam nibh a dui iaculis viverra id a velit. Vivamus egestas risus in magna varius commodo pretium porttitor lectus..</p>
<h4 class="abs foot-h" style="left:363px">Quick Links</h4>
<ul class="abs foot-list" style="left:363px"><li>Home</li><li>About us</li><li>Services</li><li>Photo Gallery</li><li>Club News</li></ul>
<ul class="abs foot-list" style="left:495px"><li>Policies</li><li>Unavailable Dates</li><li>Contact us</li></ul>
<h4 class="abs foot-h" style="left:690px">Services</h4>
<ul class="abs foot-list" style="left:690px"><li>Duis aliquam nibh</li><li>Dui iaculis</li><li>Viverra id a velit</li><li>Vivamus egestas</li><li>Risus in magna</li></ul>
<h4 class="abs foot-h" style="left:906px">Contact Info</h4>
<p class="abs foot-line" style="top:3111px;font-size:12.5px;font-weight:700;text-transform:uppercase">Birchvale Critter Den</p>
<p class="abs foot-line" style="top:3142px;width:220px;display:block">412 Fernlow Lane, Birchvale, BV2 7KD</p>
<p class="abs foot-line" style="top:3197px"><svg width="12" height="12" viewBox="0 0 24 24" fill="#fff"><path d="M5 3h4l2 5-3 2a11 11 0 0 0 6 6l2-3 5 2v4a2 2 0 0 1-2 2A17 17 0 0 1 3 5a2 2 0 0 1 2-2z"/></svg>1-800-555-0178</p>
<p class="abs foot-line" style="top:3222px"><svg width="12" height="10" viewBox="0 0 24 18"><rect x="0" y="0" width="24" height="18" fill="#fff"/><path d="M0 0l12 9 12-9" fill="none" stroke="#0b6aa3" stroke-width="2.5"/></svg>info@birchvalecritterden.com</p>

<div class="abs bottom-bar"></div>
<p class="abs copy">Copyright © 2016, Birchvale Critter Den.All Right Reserved</p>
<div class="abs socials"><span></span><span></span><span></span><span></span><span></span><span></span></div>
</body>
</html>
```